Wine Label for White and Red Wine from California

We need a wine label for 2 whites and 2 red wines. (Merlot, Cabernet Sauvignon, Chardonnay, Pinot Grigio) Can be the same label or can have something to differentiate among them such as a color change. This is a label for an already existing wine on the US market but needs to be completely re-done. We want something way sharper, eye catching. Don't use the original label please as your starting point-- I don't think we want to see it anymore. But the structure of it is ok and the fonts are ok. (The tree is what is so awful about)

Target Market(s)

US market, always good to think of millennials, but still appeal to all ages. Men and women.

Colors

Designer to choose colors to be used in the design.

Requirements
Must have
• Should be eye catching, grabs attention, looks expensive, sells for a value price. Should feature the brand name and varietal and vintage:
• Korvel Vineyards / Cabernet Sauvignon / 2014
• Bottle type is the 'Bordeaux Style' bottle. The white wine is a green bottle, the red wine uses a dark brown bottle. Be sure the labels look good on these bottles.
• What this bottle looks like is shown below.
• The label we are replacing is shown in the briefs.
Nice to have
• We feel successful labels have a lot of white background, stay away from dark labels-- they scratch too much when handled.
• Attached is a label we like, please look at the Lumbra label image below. But at the same time, we are flexible to your creativity. But nothing too crazy please.
Should not have
• Should not have a dark background.
• We are not big fans of grapes on the label unless extremely stylised. Nor do we like wine glasses, wine bottles.

```html
<!DOCTYPE html>
<html lang="en">
<head>
<meta charset="utf-8">
<title>Korvel Vineyards – Wine Labels</title>
<link rel="stylesheet" href="https://fonts.googleapis.com/css2?family=Tinos:wght@400;700&display=swap">
<style>
  :root {
    --backdrop: #e8e8e8;
    --paper: #ffffff;
    --ink-brown: #4a2a2c;
    --vine-beige: #e3dccb;
    --label-red: #c8191c;
    --vine-red: #e2403d;
    --ink-white: #ffffff;
  }
  html, body {
    margin: 0;
    padding: 0;
    overflow: hidden;
  }
  body {
    width: 1029px;
    height: 1200px;
    background: var(--backdrop);
    position: relative;
    font-family: "Tinos", "Times New Roman", serif;
  }
  .label {
    position: absolute;
    width: 341px;
    height: 474px;
    border-radius: 24px;
    overflow: hidden;
    box-shadow: 0 2px 4px rgba(0, 0, 0, 0.18);
  }
  .label svg { display: block; }
  .label text { font-family: "Tinos", "Times New Roman", serif; }
  .label--white { background: var(--paper); color: var(--ink-brown); }
  .label--red { background: var(--label-red); color: var(--ink-white); }
  .label--classic-white { left: 136px; top: 81px; }
  .label--vine-white { left: 568px; top: 81px; }
  .label--classic-red { left: 136px; top: 638px; }
  .label--vine-red { left: 568px; top: 638px; }
  .brand { font-weight: 700; fill: currentColor; }
  .regular { font-weight: 400; fill: currentColor; }
  .rule { stroke: currentColor; stroke-width: 1; }
</style>
</head>
<body>

<!-- Classic white: Chardonnay -->
<div class="label label--white label--classic-white">
  <svg width="341" height="474" viewBox="0 0 341 474">
    <text class="brand" x="171" y="196" font-size="68" text-anchor="middle" textLength="236" lengthAdjust="spacingAndGlyphs">KORVEL</text>
    <line class="rule" x1="49" y1="201.5" x2="293" y2="201.5"/>
    <text class="brand" x="49" y="240" font-size="22" textLength="244" lengthAdjust="spacingAndGlyphs">KORVEL VINEYARDS</text>
    <text class="regular" x="293" y="267" font-size="24" text-anchor="end">2014</text>
    <text class="regular" x="170.5" y="370" font-size="17" text-anchor="middle">Quality White Wines Since 1996</text>
    <line class="rule" x1="54" y1="381" x2="287" y2="381"/>
    <text class="regular" x="170.5" y="409" font-size="22.5" text-anchor="middle">CHARDONNAY</text>
  </svg>
</div>

<!-- Vine white: Pinot Grigio -->
<div class="label label--white label--vine-white">
  <svg width="341" height="474" viewBox="0 0 341 474">
    <defs>
      <radialGradient id="vine-beige-glow" cx="0.55" cy="0.45" r="0.6">
        <stop offset="0" stop-color="var(--vine-beige)" stop-opacity="0.75"/>
        <stop offset="1" stop-color="var(--vine-beige)" stop-opacity="0"/>
      </radialGradient>
    </defs>
    <rect role="img" aria-label="Stylised grapevine with leaves and curling tendrils" x="0" y="20" width="341" height="410" fill="url(#vine-beige-glow)"/>
    <text class="brand" transform="translate(185 317) rotate(-90)" font-size="80" textLength="278" lengthAdjust="spacingAndGlyphs">KORVEL</text>
    <text class="regular" transform="translate(213 317) rotate(-90)" font-size="24" textLength="278" lengthAdjust="spacing">VINEYARDS</text>
    <text class="regular" x="171" y="364" font-size="17" text-anchor="middle">Quality White Wines Since 1996</text>
    <line class="rule" x1="56" y1="377" x2="286" y2="377"/>
    <text class="regular" x="171" y="404" font-size="22.5" text-anchor="middle">PINOT GRIGIO</text>
    <text class="regular" x="171" y="431" font-size="22.5" text-anchor="middle">2014</text>
  </svg>
</div>

<!-- Classic red: Merlot -->
<div class="label label--red label--classic-red">
  <svg width="341" height="474" viewBox="0 0 341 474">
    <text class="brand" x="171" y="196" font-size="68" text-anchor="middle" textLength="236" lengthAdjust="spacingAndGlyphs">KORVEL</text>
    <line class="rule" x1="49" y1="201.5" x2="293" y2="201.5"/>
    <text class="brand" x="49" y="240" font-size="22" textLength="244" lengthAdjust="spacingAndGlyphs">KORVEL VINEYARDS</text>
    <text class="regular" x="293" y="267" font-size="24" text-anchor="end">2014</text>
    <text class="regular" x="170.5" y="370" font-size="17" text-anchor="middle">Quality Red Wines Since 1996</text>
    <line class="rule" x1="54" y1="381" x2="287" y2="381"/>
    <text class="regular" x="170.5" y="409" font-size="22.5" text-anchor="middle">MERLOT</text>
  </svg>
</div>

<!-- Vine red: Cabernet Sauvignon -->
<div class="label label--red label--vine-red">
  <svg width="341" height="474" viewBox="0 0 341 474">
    <defs>
      <radialGradient id="vine-red-glow" cx="0.55" cy="0.45" r="0.6">
        <stop offset="0" stop-color="var(--vine-red)" stop-opacity="0.8"/>
        <stop offset="1" stop-color="var(--vine-red)" stop-opacity="0"/>
      </radialGradient>
    </defs>
    <rect role="img" aria-label="Stylised grapevine with leaves and curling tendrils" x="0" y="20" width="341" height="410" fill="url(#vine-red-glow)"/>
    <text class="brand" transform="translate(185 317) rotate(-90)" font-size="80" textLength="278" lengthAdjust="spacingAndGlyphs">KORVEL</text>
    <text class="regular" transform="translate(213 317) rotate(-90)" font-size="24" textLength="278" lengthAdjust="spacing">VINEYARDS</text>
    <text class="regular" x="171" y="364" font-size="17" text-anchor="middle">Quality Red Wines Since 1996</text>
    <line class="rule" x1="56" y1="377" x2="286" y2="377"/>
    <text class="regular" x="171" y="404" font-size="22.5" text-anchor="middle">CABERNET SAUVIGNON</text>
    <text class="regular" x="171" y="431" font-size="22.5" text-anchor="middle">2014</text>
  </svg>
</div>

</body>
</html>
```